A Lantern on the pier.

I need a book cover (and back cover) design for a novel. The novel is a thiller. ´Synopsis: During the party after an awards ceremony at prestigious institution, one of the young awarders dissapear. The last place where he left a trace was close to a giant chessboard in the grass of the beautiful gardens of the place of ceremony. The detective in charge of finding the missing person and find out what happened will gradually discover that the institution is not all that it seems.
The book cover size will be 9" x 6" and the title of the novel "A lantern on the pier" will be name in spanish "Una linterna en el muelle". The back cover will have a synopsis (in spanish )that i will develop later on.
One suggestion for the design: I always love the art of MILO TRENT for movie posters, so I´m looking for something of similar style, you know (the girl who sold paper kites, North pier ballad, halvorn, ledger of shadows, etc

```html
<!DOCTYPE html>
<html lang="es">
<head>
<meta charset="utf-8">
<title>Una linterna en el muelle — Cubierta</title>
<link rel="stylesheet" href="https://fonts.googleapis.com/css2?family=Permanent+Marker&family=Luckiest+Guy&family=Roboto+Condensed:wght@400&display=swap">
<style>
  :root {
    --backdrop: #dcdcdc;
    --cover: #2c2b2d;
    --spine: #1e1d1f;
    --cream: #ece8d2;
    --red: #d94657;
    --grey-box: #c9c9c9;
    --body-text: #e4e2dc;
  }
  * { margin: 0; padding: 0; box-sizing: border-box; }
  html, body { width: 1200px; height: 857px; overflow: hidden; }
  body { background: var(--backdrop); position: relative; }

  .spread {
    position: absolute; left: 98px; top: 68px;
    width: 1004px; height: 720px;
    display: flex;
    box-shadow: 0 14px 30px rgba(0,0,0,0.25);
  }

  /* Back cover */
  .back-cover {
    width: 480px; height: 720px; background: var(--cover);
    position: relative; overflow: hidden;
  }
  .back-title {
    position: absolute; left: 30px; top: 40px; width: 420px;
    font-family: 'Permanent Marker', cursive;
    color: var(--cream); font-size: 42px; line-height: 1.1;
  }
  .back-title .sun {
    position: absolute; left: -8px; top: 4px; width: 62px; height: 62px;
    border-radius: 50%; background: var(--red); z-index: 0;
  }
  .back-title span { position: relative; z-index: 1; }
  .back-title .accent { color: var(--red); }
  .back-title .line-two { display: block; padding-left: 70px; }
  .synopsis {
    position: absolute; left: 30px; top: 195px; width: 420px;
    font-family: 'Roboto Condensed', sans-serif; font-size: 12.5px;
    line-height: 1.45; color: var(--body-text);
  }
  .synopsis p { margin-bottom: 16px; }
  .author-block {
    position: absolute; left: 30px; top: 470px; width: 420px;
    display: flex; gap: 16px;
  }
  .author-photo {
    width: 78px; height: 120px; background: var(--grey-box); flex: none;
  }
  .author-bio { font-family: 'Roboto Condensed', sans-serif; font-size: 12.5px; line-height: 1.45; color: var(--body-text); }
  .author-bio h3 {
    font-weight: 400; font-size: 16px; color: var(--red);
    text-align: center; margin-bottom: 14px;
  }

  /* Spine */
  .spine {
    width: 44px; height: 720px; background: var(--spine);
    position: relative;
  }
  .spine-title, .spine-author {
    position: absolute; left: 50%; white-space: nowrap;
    transform-origin: left top;
  }
  .spine-title {
    top: 28px; transform: translateX(11px) rotate(90deg);
    font-family: 'Permanent Marker', cursive; font-size: 20px; color: var(--cream);
  }
  .spine-title .accent { color: var(--red); }
  .spine-author {
    top: 470px; transform: translateX(12px) rotate(90deg);
    font-family: 'Luckiest Guy', sans-serif; font-size: 22px; color: var(--cream);
    letter-spacing: 1px;
  }

  /* Front cover */
  .front-cover {
    width: 480px; height: 720px; background: var(--cover);
    position: relative; overflow: hidden; text-align: center;
  }
  .front-title {
    position: absolute; left: 0; right: 0; top: 36px;
    font-family: 'Permanent Marker', cursive; color: var(--cream);
  }
  .front-title .article { display: block; font-size: 50px; line-height: 1; }
  .front-title .main-word {
    display: block; color: var(--red); font-size: 84px; line-height: 1.05;
    margin-top: 6px;
  }
  .front-title .tail { display: block; font-size: 52px; line-height: 1.1; }
  .cover-art {
    position: absolute; left: 0; top: 335px; width: 480px; height: 290px;
  }
  .front-author {
    position: absolute; left: 0; right: 0; top: 640px;
    font-family: 'Luckiest Guy', sans-serif; font-size: 46px;
    color: var(--cream); letter-spacing: 1px;
  }
</style>
</head>
<body>
  <div class="spread">
    <section class="back-cover">
      <h2 class="back-title">
        <i class="sun"></i>
        <span>Una <span class="accent">linterna</span> en el</span>
        <span class="line-two">muelle</span>
      </h2>
      <div class="synopsis">
        <p>Lorem ipsum dolor sit amet, consectetur adipiscing elit, sed do eiusmod tempor incididunt ut labore et dolore magna aliqua. Ut enim ad minim veniam, quis nostrud exercitation ullamco laboris nisi ut aliquip ex ea commodo consequat. Duis aute irure dolor in reprehenderit in voluptate velit esse cillum dolore eu fugiat nulla pariatur.</p>
        <p>Excepteur sint occaecat cupidatat non proident, sunt in culpa qui officia deserunt mollit anim id est laborum. Sed ut perspiciatis unde omnis iste natus error sit voluptatem accusantium doloremque laudantium, totam rem aperiam, eaque ipsa quae ab illo inventore veritatis et quasi architecto beatae vitae dicta sunt explicabo. Nemo enim ipsam voluptatem quia voluptas sit aspernatur aut odit aut fugit, sed quia consequuntur magni dolores eos qui ratione voluptatem sequi nesciunt.</p>
        <p>Neque porro quisquam est, qui dolorem ipsum quia dolor sit amet, consectetur, adipisci velit, sed quia non numquam eius modi tempora incidunt ut labore et dolore magnam aliquam quaerat voluptatem.</p>
      </div>
      <div class="author-block">
        <div class="author-photo" role="img" aria-label="Retrato del autor"></div>
        <div class="author-bio">
          <h3>ADRIAN VELMORE</h3>
          <p>Lorem ipsum dolor sit amet, consectetur adipiscing elit, sed do eiusmod tempor incididunt ut labore et dolore magna aliqua. Quis ipsum suspendisse ultrices gravida. Risus commodo viverra maecenas accumsan lacus vel facilisis.</p>
        </div>
      </div>
    </section>

    <section class="spine">
      <div class="spine-title">UNA <span class="accent">LINTERNA</span> EN EL MUELLE</div>
      <div class="spine-author">ADRIAN VELMORE</div>
    </section>

    <section class="front-cover">
      <h1 class="front-title">
        <span class="article">Una</span>
        <span class="main-word">LINTERNA</span>
        <span class="tail">EN EL MUELLE</span>
      </h1>
      <svg class="cover-art" viewBox="0 0 480 290" role="img" aria-label="Ilustración: piezas de ajedrez gigantes caídas sobre un tablero en el césped, un hombre de traje junto a ellas y un sol rojo">
        <defs>
          <linearGradient id="artTone" x1="0" y1="0" x2="0" y2="1">
            <stop offset="0" stop-color="#3a393b"/>
            <stop offset="1" stop-color="#6e6d70"/>
          </linearGradient>
        </defs>
        <rect x="20" y="0" width="440" height="290" fill="url(#artTone)"/>
        <circle cx="45" cy="36" r="44" fill="#d94657"/>
      </svg>
      <div class="front-author">ADRIAN VELMORE</div>
    </section>
  </div>
</body>
</html>
```